UPLIFT Group Fitness Class Launch Poster!

We need a poster design for a upcoming Group Fitness Class launch with two additional social media post designs.
Please follow our Brand Style Guide, as I will not be able to accept anything outside of this guide.
Class Description:
Come and UPLIFT your body with this class while catching up with friends and meeting new people. It is low-impact strength training with bodyweight exercises to help improve muscular strength, cardiovascular endurance, balance, bone health and functional training. It is suitable for all fitness levels.
Class Length: 30 Minutes
Intro script for class online:
📣New class alert❗
PWL team is excited to announce the launch of our new class, "UPLIFT", instructed by Jo! 🥰
Unsure if group fitness classes are for you? Join us for 30-minute low-impact strength training with bodyweight exercises! It's time to build your confidence in a fun and supportive environment.
Target Market(s)
Target audience is mostly females which barrier to entry to fitness is not having the confidence to join or has limited capability and needing low impact. Important to note that our demographic tends to be below 50... So barriers is most likely to be confidence, overweight or unfit.
Industry/Entity Type
Fitness
Font styles to use
Other font styles liked:
- Please follow the Style Guide Fonts.
Requirements
Must have
- The project must follow our Brand Guidelines & include the class logo. Poster should be exciting and stand out. Don't necessarily have to use the stock images provided.
Should not have
- If you select your own image, the preference would be that it does not only include slim/fit looking individuals.

```html
<!DOCTYPE html>
<html lang="en">
<head>
<meta charset="utf-8">
<title>UPLIFT – New Group Fitness Class</title>
<link rel="stylesheet" href="https://fonts.googleapis.com/css2?family=Montserrat:wght@900&family=Roboto:ital,wght@0,400;0,500;0,700;0,900;1,500&family=Libre+Baskerville&display=swap">
<style>
  :root {
    --red-deep: #6e1624;
    --red-mid: #8c1f30;
    --red-warm: #a52637;
    --brand-red: #a3202f;
    --ink: #1f1f1f;
    --paper: #ffffff;
  }
  * { margin: 0; padding: 0; box-sizing: border-box; }
  html, body { width: 848px; height: 1200px; overflow: hidden; background: var(--red-deep); }
  .poster {
    position: relative; width: 848px; height: 1200px; overflow: hidden;
    font-family: "Roboto", Arial, sans-serif; color: var(--paper);
  }
  .backdrop {
    position: absolute; inset: 0;
    background:
      radial-gradient(ellipse at 30% 35%, rgba(190,50,65,.55), transparent 60%),
      radial-gradient(ellipse at 70% 85%, rgba(170,40,55,.5), transparent 55%),
      linear-gradient(160deg, var(--red-mid) 0%, var(--red-deep) 55%, var(--red-warm) 100%);
  }
  .title-stack { position: absolute; inset: 0; }
  .title-face { font-family: "Montserrat", sans-serif; font-weight: 900; }
  .title-solid { fill: var(--paper); }
  .title-note { font-family: "Libre Baskerville", Georgia, serif; fill: var(--paper); }

  .info-panel { position: absolute; left: 448px; top: 0; width: 332px; height: 712px; }
  .info-panel svg { position: absolute; inset: 0; }

  .brand { position: absolute; left: 482px; top: 100px; width: 262px; display: flex; align-items: center; gap: 10px; color: var(--ink); }
  .brand-dot { width: 46px; height: 46px; border-radius: 50%; background: var(--brand-red); flex: none; }
  .brand-name { font-size: 24px; line-height: 1.1; font-weight: 500; }
  .brand-name small { display: block; font-size: 10px; letter-spacing: 1.6px; margin-top: 4px; font-weight: 500; }

  .length { position: absolute; left: 480px; top: 290px; width: 266px; height: 93px;
    border-top: 1.5px solid var(--ink); border-bottom: 1.5px solid var(--ink); text-align: center; }
  .length-label { margin-top: 14px; font-size: 24px; color: var(--ink); }
  .length-value { font-size: 31px; font-weight: 900; letter-spacing: 5px; color: var(--brand-red); line-height: 1.2; }

  .description { position: absolute; right: 102px; top: 410px; text-align: right; white-space: nowrap;
    color: var(--ink); font-size: 19px; line-height: 24px; }

  .alert { position: absolute; left: 458px; top: 692px; width: 312px; height: 146px;
    background: var(--brand-red); border: 1.5px solid var(--paper); border-radius: 16px; text-align: center; }
  .alert-title { height: 56px; display: flex; align-items: center; justify-content: center; gap: 8px;
    font-size: 25px; font-weight: 700; border-bottom: 1.5px solid var(--paper); }
  .alert-body { padding-top: 14px; font-size: 15px; line-height: 19px; }
  .alert-body strong { display: block; font-size: 18px; line-height: 24px; font-weight: 700; }

  .unsure { position: absolute; right: 88px; top: 922px; text-align: right; }
  .unsure-head { font-size: 72px; font-weight: 900; line-height: 1; letter-spacing: -1px; }
  .unsure-sub { margin-top: 8px; font-size: 16px; font-weight: 700; letter-spacing: 4.2px; line-height: 20px; }
  .unsure-copy { margin-top: 16px; white-space: nowrap; font-size: 15.5px; font-style: italic; font-weight: 500; line-height: 19.6px; }
</style>
</head>
<body>
<main class="poster">
  <div class="backdrop" role="img" aria-label="Photo of a diverse group of people doing bodyweight squats in a gym, tinted red"></div>

  <svg class="title-stack" width="848" height="1200" viewBox="0 0 848 1200" aria-label="Come and UPLIFT with us">
    <defs>
      <mask id="outline-words" maskUnits="userSpaceOnUse" x="0" y="0" width="848" height="1200">
        <rect width="848" height="1200" fill="#000"/>
        <g transform="rotate(-90)" class="title-face">
          <g fill="#fff" stroke="#fff" stroke-width="4.4" stroke-linejoin="round">
            <text x="-1012" y="180" font-size="146" textLength="772" lengthAdjust="spacingAndGlyphs">COME &amp;</text>
            <text x="-684" y="424" font-size="96" textLength="540" lengthAdjust="spacingAndGlyphs">WITH US</text>
          </g>
          <g fill="#000">
            <text x="-1012" y="180" font-size="146" textLength="772" lengthAdjust="spacingAndGlyphs">COME &amp;</text>
            <text x="-684" y="424" font-size="96" textLength="540" lengthAdjust="spacingAndGlyphs">WITH US</text>
          </g>
        </g>
      </mask>
    </defs>
    <rect width="848" height="1200" fill="#ffffff" mask="url(#outline-words)"/>
    <g transform="rotate(-90)">
      <text class="title-face title-solid" x="-1124" y="336" font-size="188" textLength="1048" lengthAdjust="spacingAndGlyphs">UPLIFT</text>
      <text class="title-note" x="-1124" y="374" font-size="19" textLength="280" lengthAdjust="spacingAndGlyphs">Intro Script For Class Online</text>
    </g>
  </svg>

  <div class="info-panel">
    <svg width="332" height="712" viewBox="0 0 332 712">
      <path fill="#ffffff" d="M10 0 H326 L322 40 L328 90 L320 150 L327 210 L321 270 L328 330 L322 400 L327 470 L320 540 L326 610 L321 712 H14 L8 650 L14 590 L6 520 L13 450 L7 380 L14 310 L6 240 L13 170 L7 100 L14 40 Z"/>
    </svg>
  </div>

  <div class="brand">
    <span class="brand-dot"></span>
    <p class="brand-name">Shire of West Karrow<small>RECREATION &amp; FITNESS</small></p>
  </div>

  <div class="length">
    <p class="length-label">CLASS LENGTH</p>
    <p class="length-value">30 MINUTES</p>
  </div>

  <p class="description">with this class while catching<br>up with friends and meeting<br>new people. It is low-impact<br>strength training with<br>bodyweight exercises to help<br>improve muscular strength,<br>cardiovascular endurance,<br>balance, bone health and<br>functional training. It is<br>suitable for all fitness levels.</p>

  <section class="alert">
    <h2 class="alert-title">NEW CLASS ALERT
      <svg width="30" height="24" viewBox="0 0 30 24" aria-hidden="true"><path d="M8 8 L20 3 V21 L8 16 Z M4 8 H8 V16 H4 Z M11 16 L13 22" fill="none" stroke="#fff" stroke-width="2" stroke-linejoin="round"/><path d="M23 8 Q26 12 23 16" fill="none" stroke="#fff" stroke-width="2"/></svg>
    </h2>
    <p class="alert-body">PWL team is excited to announce<br>the launch of our new class,<strong>"UPLIFT", instructed by Jo!</strong></p>
  </section>

  <section class="unsure">
    <h2 class="unsure-head">UNSURE</h2>
    <p class="unsure-sub">IF GROUP FITNESS<br>CLASSES ARE FOR YOU?</p>
    <p class="unsure-copy">Join us for 30-minute low-impact strength<br>training with body weight exercises!<br>It's time to build your confidence in a fun<br>and supportive environment.</p>
  </section>
</main>
</body>
</html>
```